Business Card Upgrade

I have designed our business card using our new logo. I think it needs imporovements. We used to have two cards for our business. One card was for our software business, and the other was for our consulting business. We are now in the process of combining our websites, marketing, name, and a new logo.

Our goal is to have a really sharp professional logo. One reason I designed the card the way I did was that our Titles are sometimes long, and by separating the person's name and title, it shows up very well and the title can be adjusted no matter how long it is. Sometimes the title can be 4 or 5 words or more.

We really like our logo on black as it shows up very nice. Our PMS colors are as follows: 368C and 459C.

The Designer that will be working with us will need to deliver the following:

The front and back of the Business Card Design will need to be delivered in a high quality JPEG, and
The front and back of the Business Card Design in Illustrator Format .ai
Any fonts will need to be sent to us if they are not standard and are required to open the Illustrator file correctly.

To help us get a good idea of the card with a title, please use the title: " Director of Software Development "

NOTE: The chosen designer will be selected to design our new letterhead within 2 weeks from the closing of this contest.

To help us make sure the card design works with longer titles, please use the followign job title on the card:  

"Director of Software and Product Development"

 

ALL DESIGNERS:

1. I appreciate the different angles you are showing the cards, but please be sure and always show the direct view, so I can see the layout and what the person I hand the card will see.

2. Please do not use white.  Please use off white as I don't care for white cards and they get dirty easy and do not represent the designs well.

Dear Designers,

Please provide samples straight one as a viewer of the card will see.  Some of the angles that are presented make it impossible to tell how everything fits, and sometimes even makes areas look skewed. So, please provide a straight sample view.

Pinnacle 400 company executives such as Vice Presidents, and Directors

Software

• Professional looking Card.

Our customers are Directors, Vice Presidents, and Presidents of companies as large as Pinnacle 400 companies. The card needs to get attention wile still looking professional.

Delivery of the finished product in Illustrator Format with any fonts needed to edit the text or open the file.

The card will be a heavy stock with a soft touch coating for that silk feel.

```html
<!DOCTYPE html>
<html lang="en">
<head>
<meta charset="utf-8">
<title>Harborline Trade Company — Business Card</title>
<link rel="stylesheet" href="https://fonts.googleapis.com/css2?family=Roboto+Condensed:wght@400;700&display=swap">
<style>
  :root {
    --card-black: #000000;
    --card-gold: #e2cf8b;
    --brand-green: #5aa844;
    --ink-dark: #111111;
    --page-bg: #ffffff;
  }
  html, body {
    margin: 0;
    padding: 0;
    width: 1017px;
    height: 1200px;
    overflow: hidden;
    background: var(--page-bg);
    font-family: "Roboto Condensed", "Arial Narrow", sans-serif;
  }
  .canvas {
    position: relative;
    width: 1017px;
    height: 1200px;
  }
  .card {
    position: absolute;
    left: 151px;
    width: 721px;
    height: 400px;
  }
  .card-front {
    top: 148px;
    background: var(--card-black);
    display: flex;
    align-items: center;
    justify-content: center;
  }
  .brand-name {
    margin: 0;
    color: var(--brand-green);
    font-weight: 700;
    text-transform: uppercase;
    text-align: center;
    line-height: 1.1;
  }
  .card-front .brand-name {
    font-size: 41px;
    letter-spacing: 3px;
  }
  .card-back {
    top: 655px;
    background: var(--card-gold);
  }
  .contact-panel {
    position: absolute;
    left: 39px;
    top: 0;
    width: 243px;
    height: 400px;
    background: var(--card-black);
  }
  .contact-panel .brand-name {
    position: absolute;
    left: 22px;
    width: 200px;
    top: 44px;
    font-size: 22px;
    letter-spacing: 1px;
    text-align: center;
  }
  .contact-list {
    position: absolute;
    left: 24px;
    top: 185px;
    margin: 0;
    color: var(--card-gold);
    font-size: 21px;
    line-height: 31px;
    font-style: normal;
  }
  .website {
    position: absolute;
    left: 30px;
    top: 348px;
    margin: 0;
    color: var(--brand-green);
    font-size: 22px;
  }
  .tagline {
    position: absolute;
    left: 300px;
    top: 54px;
    margin: 0;
    color: var(--ink-dark);
    font-size: 21px;
    line-height: 27px;
    text-transform: uppercase;
  }
  .person {
    position: absolute;
    right: 43px;
    top: 250px;
    text-align: right;
    color: var(--ink-dark);
  }
  .person-name {
    margin: 0;
    font-size: 50px;
    font-weight: 700;
    line-height: 1;
  }
  .person-title {
    margin: 10px 0 0;
    font-size: 20px;
    line-height: 23px;
  }
</style>
</head>
<body>
  <main class="canvas">
    <section class="card card-front" aria-label="Card front">
      <h1 class="brand-name">Harborline<br>Trade Company</h1>
    </section>

    <section class="card card-back" aria-label="Card back">
      <div class="contact-panel">
        <p class="brand-name">Harborline<br>Trade Company</p>
        <address class="contact-list">
          1480 Bayview Road<br>
          Mobile, AL 36604<br>
          251.555.0147 (Direct)<br>
          dreyes@harborline.com
        </address>
        <p class="website">www.harborline.com</p>
      </div>

      <p class="tagline">One partner with the depth and skill<br>to handle every trade zone need</p>

      <div class="person">
        <h2 class="person-name">Daniel Reyes</h2>
        <p class="person-title">Director of Software and<br>Product Development</p>
      </div>
    </section>
  </main>
</body>
</html>
```